Packaging design for a low carb bar

I am producing a low carb / high fat bar, therefore I would like to have a light weighted modern design. The background color pastel light or something like that. The package should be focused on fitness-active individuals who are looking for healthy low carb snacks. Preliminary packaging size, logo, and more details on what should be attached to the packaging are attached. Thank you!

```html
<!DOCTYPE html>
<html lang="en">
<head>
<meta charset="utf-8">
<title>Low Carb Bar Wrapper – Flat Dieline</title>
<link rel="stylesheet" href="https://fonts.googleapis.com/css2?family=Dosis:wght@400;600&display=swap">
<style>
  :root {
    --wrapper-blue: #6ccbea;
    --fold-line: #3c4650;
    --title-ink: #0d0f11;
    --flavour-ink: #103a48;
    --badge-teal: #8fd9e2;
    --badge-yellow: #ffe14a;
    --claim-cream: #f4e7b0;
    --photo-light: #9ea3a6;
    --photo-dark: #141516;
    --seal-mark: #1d1d1f;
    --dimension-ink: #444;
    --page: #ffffff;
  }
  html, body {
    margin: 0;
    width: 1200px;
    height: 1200px;
    overflow: hidden;
    background: var(--page);
  }
  .dieline {
    display: block;
    position: absolute;
    top: 272px;
    left: 0;
    width: 1200px;
    height: 656px;
  }
  .wrapper-face { fill: var(--wrapper-blue); stroke: var(--fold-line); stroke-width: 1.2; }
  .fold-line { stroke: var(--fold-line); stroke-width: 1.2; }
  .seal-mark { fill: var(--seal-mark); }
  .product-title {
    font-family: "Dosis", sans-serif;
    font-weight: 600;
    font-size: 66px;
    fill: var(--title-ink);
    letter-spacing: 1px;
  }
  .flavour-line {
    font-family: "Dosis", sans-serif;
    font-weight: 600;
    font-size: 27px;
    fill: var(--flavour-ink);
  }
  .photo-window { stroke: #ffffff; stroke-width: 4; }
  .brand-disc { fill: var(--badge-teal); stroke: #ffffff; stroke-width: 2; }
  .brand-name {
    font-family: "Dosis", sans-serif;
    font-weight: 600;
    font-size: 13px;
    fill: #ffffff;
    letter-spacing: 1px;
  }
  .claim-box { fill: rgba(255,255,255,.12); stroke: #e6e9ea; stroke-width: 1.5; }
  .claim-vegan { font-family: "Dosis", sans-serif; font-weight: 600; font-size: 22px; fill: var(--badge-teal); }
  .claim-carbs { font-family: "Dosis", sans-serif; font-weight: 600; font-size: 17px; fill: var(--badge-yellow); }
  .claim-diet { font-family: "Dosis", sans-serif; font-weight: 600; font-size: 17px; fill: var(--claim-cream); }
  .dim-line { stroke: var(--dimension-ink); stroke-width: 1.2; }
  .dim-label { font-family: "Dosis", sans-serif; font-weight: 400; font-size: 17px; fill: var(--dimension-ink); }
</style>
</head>
<body>
<svg class="dieline" viewBox="0 0 1500 820" xmlns="http://www.w3.org/2000/svg">
  <defs>
    <linearGradient id="photo-fill" x1="0" y1="0" x2="0" y2="1">
      <stop offset="0" stop-color="#4a4d50"/>
      <stop offset=".45" stop-color="var(--photo-light)"/>
      <stop offset="1" stop-color="var(--photo-dark)"/>
    </linearGradient>
  </defs>

  <rect class="wrapper-face" x="307" y="24" width="806" height="718"/>
  <g class="fold-lines">
    <line class="fold-line" x1="307" y1="43" x2="1113" y2="43"/>
    <line class="fold-line" x1="307" y1="104" x2="1113" y2="104"/>
    <line class="fold-line" x1="307" y1="197" x2="1113" y2="197"/>
    <line class="fold-line" x1="307" y1="290" x2="1113" y2="290"/>
    <line class="fold-line" x1="307" y1="476" x2="1113" y2="476"/>
    <line class="fold-line" x1="307" y1="569" x2="1113" y2="569"/>
    <line class="fold-line" x1="307" y1="662" x2="1113" y2="662"/>
    <line class="fold-line" x1="307" y1="723" x2="1113" y2="723"/>
  </g>
  <rect class="seal-mark" x="307" y="662" width="31" height="61"/>

  <path class="photo-window" fill="url(#photo-fill)" role="img"
        aria-label="Photo of a runner's legs in sports shoes against a concrete wall"
        d="M900,177 C1010,245 1058,350 1050,420 C1040,505 980,572 900,636 C820,572 760,505 752,420 C746,345 800,245 900,177Z"/>

  <text class="product-title" x="428" y="398">KETO BAR</text>
  <text class="flavour-line" x="444" y="432">almond/coconut/chia</text>

  <circle class="brand-disc" cx="795" cy="357" r="47"/>
  <text class="brand-name" x="795" y="353" text-anchor="middle">VELA</text>
  <text class="brand-name" x="795" y="370" text-anchor="middle">NUTRITION</text>

  <rect class="claim-box" x="847" y="366" width="96" height="28" rx="4"/>
  <text class="claim-vegan" x="895" y="387" text-anchor="middle">vegan</text>
  <rect class="claim-box" x="945" y="380" width="84" height="46" rx="4"/>
  <text class="claim-carbs" x="987" y="399" text-anchor="middle">3.5g</text>
  <text class="claim-carbs" x="987" y="420" text-anchor="middle">net carbs</text>
  <rect class="claim-box" x="768" y="412" width="174" height="50" rx="4"/>
  <text class="claim-diet" x="855" y="433" text-anchor="middle">suitable for a keto</text>
  <text class="claim-diet" x="855" y="455" text-anchor="middle">LCHF diet</text>

  <g class="dimensions">
    <line class="dim-line" x1="1181" y1="24" x2="1181" y2="742"/>
    <line class="dim-line" x1="1143" y1="24" x2="1217" y2="24"/>
    <line class="dim-line" x1="1143" y1="43" x2="1217" y2="43"/>
    <line class="dim-line" x1="1143" y1="104" x2="1217" y2="104"/>
    <line class="dim-line" x1="1143" y1="197" x2="1217" y2="197"/>
    <line class="dim-line" x1="1143" y1="290" x2="1217" y2="290"/>
    <line class="dim-line" x1="1143" y1="476" x2="1217" y2="476"/>
    <line class="dim-line" x1="1143" y1="569" x2="1217" y2="569"/>
    <line class="dim-line" x1="1143" y1="662" x2="1217" y2="662"/>
    <line class="dim-line" x1="1143" y1="723" x2="1217" y2="723"/>
    <line class="dim-line" x1="1143" y1="742" x2="1217" y2="742"/>
    <text class="dim-label" transform="translate(1171 74) rotate(-90)" text-anchor="middle">10mm</text>
    <text class="dim-label" transform="translate(1171 151) rotate(-90)" text-anchor="middle">15mm</text>
    <text class="dim-label" transform="translate(1171 244) rotate(-90)" text-anchor="middle">15mm</text>
    <text class="dim-label" transform="translate(1171 383) rotate(-90)" text-anchor="middle">30mm</text>
    <text class="dim-label" transform="translate(1171 522) rotate(-90)" text-anchor="middle">15mm</text>
    <text class="dim-label" transform="translate(1171 615) rotate(-90)" text-anchor="middle">15mm</text>
    <text class="dim-label" transform="translate(1171 692) rotate(-90)" text-anchor="middle">10mm</text>

    <line class="dim-line" x1="307" y1="793" x2="1113" y2="793"/>
    <line class="dim-line" x1="307" y1="755" x2="307" y2="805"/>
    <line class="dim-line" x1="1113" y1="755" x2="1113" y2="805"/>
    <text class="dim-label" x="695" y="785" text-anchor="middle">130mm</text>
  </g>
</svg>
</body>
</html>
```